Create an awesome website for a medical clinic

This is a new website for a doctor's office. The site should be clean and modern, easy to navigate.

This is a wellness clinic, we want to help our clients have a healthy, active lifestyle. It should be friendly and inviting, and easy for them to call or schedule an appointment.

The site should be responsive and designed using the attached Bootstrap 3 PSD.

We will provide stock photos, until then please use stock photos from:

photoharvestbin.net or
lumapicturevault.net (preferred)

Some example sites of clean and modern designs that we like:

https://tarnelspine.example/
http://walkpastjoints.example/
http://feelingbrisker.example/

Also attached is a temporary logo you can use.
Updates

Reason: Thank you everyone for your great designs - we need a little more time so I'm extending the project.

Need extra days to review

Also, the colors in the new logo I just linked to are the final colors of the logo, so feel free to use any complimentary colors to it.

Hi everyone, The boss wants to change the layout of the site a little bit - here's the revised layout: https://www.filecrate.example/s/q8vn31kd2pxe74rt/memo%2011_29_2017.pdf?dl=0 And the graphic assets you can use are here: https://www.filecrate.example/s/q8vn31kd2pxe74rt/memo%2011_29_2017.pdf?dl=0 Feel free to change the background color of the "topbar", and change the icons of the "why people trust us" if you want, these are just temporary placeholders. Thanks for your patience and hard work!

Target Market(s)

People seeking medical treatment (wellness clinic)

Industry/Entity Type

Doctor

Number of Pages Required

1 page

Font styles to use
Sans Serif

Colors
0592cd
33a6d7
abd037
9bcb3c

Requirements
Must have
• The home page should have: a strong hero image/slideshow, clinic phone number should be prominent and at the top of the page (in the nav), a "what to expect" section (this is like a FAQs section - see attachment), and a strong call to action (a button to call or schedule an appointment).
• The what to expect section is useful so that prospective clients can determine if we're a good fit for them or not. It's a basic, first-step pre-qualification block of information.
• Social media icons which links to our social media profiles should be included.
Nice to have
• - Link to 3 most recent blog entries
• - Testimonials
• - How a multilevel nav menu looks.

```html
<!DOCTYPE html>
<html lang="en">
<head>
<meta charset="utf-8">
<title>Fernly Medical Clinic</title>
<link href="https://fonts.googleapis.com/css2?family=Montserrat:wght@500;600;700&family=Open+Sans:wght@400;600;700&display=swap" rel="stylesheet">
<style>
:root{
  --blue:#0592cd;
  --blue-soft:#33a6d7;
  --green:#9bcb3c;
  --green-light:#abd037;
  --ink:#222;
  --text:#555;
  --muted:#888;
  --line:#d9d9d9;
  --grey-head:#707070;
  --footer:#262626;
  --white:#fff;
}
*{box-sizing:border-box;margin:0;padding:0}
html,body{width:1200px;height:3333px;overflow:hidden}
body{font-family:"Open Sans",Arial,sans-serif;color:var(--text);background:var(--white);position:relative}
.section{position:absolute;left:0;width:1200px}
h2.title{font-family:"Montserrat",Arial,sans-serif;font-weight:700;font-size:34px;color:var(--ink);letter-spacing:.5px;text-transform:uppercase}
.btn-ghost{display:inline-block;border:2px solid var(--white);border-radius:28px;color:var(--white);font-family:"Montserrat",Arial,sans-serif;font-weight:700;font-size:15px;letter-spacing:.5px;text-transform:uppercase;text-align:center}

/* header */
.topline{position:absolute;top:0;left:0;width:1200px;height:5px;background:var(--blue-soft)}
.header{top:5px;height:102px;background:var(--white)}
.brand{position:absolute;left:98px;top:10px;font-weight:700;color:var(--green);line-height:1}
.brand .name{font-size:54px;letter-spacing:1px;display:block}
.brand .sub{font-size:26px;display:block;margin-top:4px;color:var(--green)}
.call{position:absolute;right:98px;top:18px;font-family:"Montserrat",Arial,sans-serif;font-size:19px;font-weight:700;color:var(--ink);display:flex;align-items:center;gap:10px}
.call .num{color:var(--blue-soft);font-weight:600}
.call svg{width:30px;height:30px}
.nav{position:absolute;right:98px;top:66px;display:flex;gap:34px;font-family:"Montserrat",Arial,sans-serif;font-size:16px;font-weight:600;color:var(--ink);text-transform:uppercase;align-items:center}
.nav .active{color:var(--green);position:relative}
.nav .active::after{content:"";position:absolute;left:50%;margin-left:-14px;top:30px;border:14px solid transparent;border-top:16px solid var(--green);border-bottom:0}

/* hero */
.hero{top:107px;height:444px;background:linear-gradient(180deg,#c9b79a 0%,#a69772 40%,#8c8a5d 70%,#b9a783 100%)}
.hero .runner{position:absolute;left:650px;top:0;width:320px;height:444px;background:linear-gradient(180deg,#c99a85,#2aa9a8 55%,#1e9c9a)}
.hero .cta{position:absolute;left:98px;top:275px;width:270px;height:50px;line-height:46px}
.dots{position:absolute;display:flex;gap:6px}
.dots i{width:12px;height:12px;border-radius:50%;border:2px solid var(--white);display:block}
.dots i.on{background:var(--white)}
.hero .dots{left:565px;top:383px}
.mega{position:absolute;left:98px;top:107px;width:1002px;height:271px;background:var(--white);box-shadow:0 4px 10px rgba(0,0,0,.15);display:flex;padding:38px 0 0 56px}
.mega ul{list-style:none;width:325px}
.mega li{font-size:14.5px;color:#444;height:32.5px;display:flex;align-items:center;gap:14px}
.mega li svg{width:15px;height:15px;flex:none}

/* welcome */
.welcome{top:551px;height:482px}
.welcome h2{position:absolute;left:98px;top:90px}
.welcome p{position:absolute;left:98px;width:440px;font-size:14px;line-height:28px}
.welcome .p1{top:146px}
.welcome .p2{top:226px}
.welcome .more{position:absolute;left:98px;top:334px;width:142px;height:44px;border:2px solid var(--line);border-radius:24px;color:var(--green);font-family:"Montserrat",Arial,sans-serif;font-weight:700;font-size:14px;text-align:center;line-height:40px}
.welcome .frame{position:absolute;left:604px;top:73px;width:507px;height:334px;border:2px solid var(--blue-soft);padding:10px}
.welcome .frame div{width:100%;height:100%;background:linear-gradient(120deg,#f2f4f5,#dfe7ea 45%,#9fc7d6 70%,#e8ecee)}

/* help band */
.help{top:1033px;height:358px;background:linear-gradient(90deg,#9bc93e,#a7cf3a 50%,#93c53c);text-align:center;color:var(--white)}
.help h2{color:var(--white);position:absolute;left:0;width:1200px;top:64px}
.help p{position:absolute;left:205px;width:790px;top:122px;font-size:14px;line-height:28px;color:#f4f9e8}
.help .btn-ghost{position:absolute;left:465px;top:233px;width:268px;height:52px;line-height:48px}

/* blog */
.blog{top:1391px;height:591px}
.blog h2{position:absolute;left:0;width:1200px;text-align:center;top:78px}
.card{position:absolute;top:156px;width:315px}
.card .ph{height:184px}
.card h3{font-family:"Montserrat",Arial,sans-serif;font-size:19px;font-weight:700;color:var(--ink);margin-top:30px}
.card .meta{display:flex;gap:16px;font-size:13px;color:var(--text);margin-top:12px;align-items:center}
.card .meta span{display:flex;align-items:center;gap:6px}
.card .meta svg{width:13px;height:13px}
.card p{font-size:13.5px;line-height:24px;margin-top:14px}
.card .rm{display:block;margin-top:12px;font-family:"Montserrat",Arial,sans-serif;font-size:13px;font-weight:700;color:var(--green)}

/* testimonials */
.testi{top:1982px;height:391px;background:linear-gradient(90deg,#3a9fd0,#4eb0dc 50%,#3f9fc9)}
.testi h2{color:var(--white);position:absolute;left:0;width:1200px;text-align:center;top:68px}
.arrow{position:absolute;top:202px;width:36px;height:36px;border:2px solid rgba(255,255,255,.7);border-radius:50%}
.arrow svg{width:100%;height:100%}
.quote{position:absolute;top:150px;width:330px;color:var(--white)}
.quote .avatar{position:absolute;left:0;top:0;width:76px;height:76px;border-radius:50%;border:3px solid var(--white);background:linear-gradient(160deg,#e8d7cc,#b79c8b)}
.quote .body{position:absolute;left:92px;top:10px;width:240px;font-style:italic;font-size:11.5px;line-height:24px;color:#e6f4fb}
.quote .who{position:absolute;left:92px;top:120px;font-size:10.5px;font-weight:700;text-transform:uppercase}
.quote .role{position:absolute;left:92px;top:140px;font-size:10px;font-style:italic;width:260px}
.quote .stars{position:absolute;left:92px;top:168px;display:flex;gap:4px}
.quote .stars svg{width:18px;height:18px}

/* what to expect */
.expect{top:2373px;height:422px}
.expect h2{position:absolute;left:0;width:1200px;text-align:center;top:76px}
.qa{position:absolute;top:154px;width:315px;height:149px;border:1px solid var(--line)}
.qa .head{height:34px;background:var(--grey-head);color:var(--white);font-family:"Montserrat",Arial,sans-serif;font-weight:600;font-size:15px;line-height:34px;padding-left:16px}
.qa.hl .head{background:var(--green)}
.qa p{padding:18px 20px 0 20px;font-size:13.5px;line-height:25px}
.expect .dots{left:579px;top:332px}
.expect .dots i{border-color:#999}
.expect .dots i.on{background:#999}

/* footer */
.footer{top:2795px;height:538px;background:linear-gradient(180deg,#2e2e2e,#232323 60%,#1f1f1f);color:var(--white)}
.totop{position:absolute;left:567px;top:32px;width:66px;text-align:center;font-family:"Montserrat",Arial,sans-serif;font-size:12px;font-weight:700}
.totop svg{display:block;width:66px;height:26px}
.footer h4{position:absolute;top:134px;font-family:"Montserrat",Arial,sans-serif;font-size:21px;font-weight:700;text-transform:uppercase}
.field{position:absolute;background:var(--white);color:#777;font-size:11.5px;padding:8px 10px}
.submit{position:absolute;left:638px;top:389px;width:90px;height:34px;border-radius:18px;background:var(--green);color:var(--white);font-family:"Montserrat",Arial,sans-serif;font-weight:700;font-size:13px;text-align:center;line-height:34px}
.info{position:absolute;left:780px;display:flex;align-items:center;gap:22px;font-size:12.5px}
.info .ic{width:34px;height:34px;border:1.5px solid #888;border-radius:50%;display:flex;align-items:center;justify-content:center}
.info .ic svg{width:16px;height:16px}
.social{position:absolute;left:782px;top:365px;display:flex;gap:10px}
.social span{width:30px;height:30px;border-radius:50%;display:block}
.footer .rule{position:absolute;left:98px;top:460px;width:1004px;height:1px;background:#444}
.copy{position:absolute;left:0;width:1200px;top:491px;text-align:center;font-size:12px;color:#ccc}
</style>
</head>
<body>
<svg width="0" height="0" style="position:absolute">
  <defs>
    <symbol id="tick" viewBox="0 0 16 16"><circle cx="8" cy="8" r="8" fill="#33a6d7"/><path d="M4.5 8.3l2.3 2.3 4.7-4.8" fill="none" stroke="#fff" stroke-width="2"/></symbol>
    <symbol id="star" viewBox="0 0 20 20"><path d="M10 1.5l2.6 5.4 5.9.8-4.3 4.1 1 5.8L10 14.8l-5.2 2.8 1-5.8L1.5 7.7l5.9-.8z" fill="#9bcb3c"/></symbol>
    <symbol id="star-o" viewBox="0 0 20 20"><path d="M10 1.5l2.6 5.4 5.9.8-4.3 4.1 1 5.8L10 14.8l-5.2 2.8 1-5.8L1.5 7.7l5.9-.8z" fill="none" stroke="#9bcb3c" stroke-width="1.5"/></symbol>
    <symbol id="cal" viewBox="0 0 14 14"><rect x="1" y="2" width="12" height="11" fill="#33a6d7"/><rect x="2.5" y="5" width="9" height="6.5" fill="#fff"/></symbol>
    <symbol id="user" viewBox="0 0 14 14"><circle cx="7" cy="4" r="3" fill="#33a6d7"/><path d="M1.5 13.5c0-3.5 2.5-5 5.5-5s5.5 1.5 5.5 5z" fill="#33a6d7"/></symbol>
    <symbol id="phone" viewBox="0 0 16 16"><path d="M4 1.5l2.2 3-1.4 1.6c.9 2 2.6 3.7 4.6 4.6l1.6-1.4 3 2.2-1.3 2.3C7.6 13.4 2.6 8.4 1.7 3z" fill="currentColor"/></symbol>
  </defs>
</svg>

<div class="topline"></div>
<header class="section header">
  <div class="brand"><span class="name">FERNLY</span><span class="sub">MEDICAL CLINIC</span></div>
  <div class="call">
    <svg viewBox="0 0 30 30"><circle cx="15" cy="15" r="13.5" fill="none" stroke="#9bcb3c" stroke-width="1.5"/><svg x="7" y="7" width="16" height="16" viewBox="0 0 16 16" style="color:#9bcb3c"><use href="#phone"/></svg></svg>
    <span>CALL : <span class="num">1 888 555 0142</span></span>
  </div>
  <nav class="nav">
    <span>Home</span><span>About</span><span class="active">Services</span><span>Testimonials</span><span>Resources</span><span>Contact Us</span>
    <svg width="16" height="16" viewBox="0 0 16 16"><circle cx="6.5" cy="6.5" r="4.8" fill="none" stroke="#222" stroke-width="2.2"/><path d="M10 10l4.5 4.5" stroke="#222" stroke-width="2.4"/></svg>
  </nav>
</header>

<section class="section hero" role="img" aria-label="Slideshow photo of a woman jogging through a sunny coastal meadow">
  <div class="runner"></div>
  <span class="btn-ghost cta">Schedule an Appointment</span>
  <div class="dots"><i class="on"></i><i></i><i></i><i></i></div>
</section>

<div class="mega">
  <ul>
    <li><svg><use href="#tick"/></svg>Cardiology</li>
    <li><svg><use href="#tick"/></svg>Dentistry</li>
    <li><svg><use href="#tick"/></svg>Dermatology &amp; Cosmetology</li>
    <li><svg><use href="#tick"/></svg>Dietetics</li>
    <li><svg><use href="#tick"/></svg>Endocrinology</li>
    <li><svg><use href="#tick"/></svg>ENT (Ear, Nose &amp; Throat)</li>
  </ul>
  <ul>
    <li><svg><use href="#tick"/></svg>Gastroenterology &amp; Hepatology</li>
    <li><svg><use href="#tick"/></svg>General Medicine</li>
    <li><svg><use href="#tick"/></svg>General Surgery</li>
    <li><svg><use href="#tick"/></svg>Obstetrics and Gynaecology</li>
    <li><svg><use href="#tick"/></svg>Ophthalmology</li>
    <li><svg><use href="#tick"/></svg>Orthopedics</li>
  </ul>
  <ul>
    <li><svg><use href="#tick"/></svg>Pediatrics</li>
    <li><svg><use href="#tick"/></svg>Plastic Surgery</li>
    <li><svg><use href="#tick"/></svg>Psychiatry</li>
    <li><svg><use href="#tick"/></svg>Radiology</li>
    <li><svg><use href="#tick"/></svg>Pathology &amp; Laboratory Sciences</li>
    <li><svg><use href="#tick"/></svg>Family Medicine</li>
  </ul>
</div>

<section class="section welcome">
  <h2 class="title">Welcome to Fernly</h2>
  <p class="p1">Nam libero tempore, cum soluta nobis est eligendi optio cumque nihil impedit quo minus id quod maxime placeat.</p>
  <p class="p2">Fere possimus, omnis voluptas assumenda est, omnis dolor repellen dus. Temporibus autem quibusdam et aut officiis debitis aut rerum necessitatibus saepe eveniet ut et voluptates.</p>
  <span class="more">READ MORE</span>
  <div class="frame"><div role="img" aria-label="Photo of a nurse and doctor caring for a senior patient in a bright clinic room"></div></div>
</section>

<section class="section help" role="region" aria-label="How can we help you">
  <h2 class="title">How can we help you</h2>
  <p>Nam libero tempore, cum soluta nobis est eligendi optio cumque nihil impedit quo minus id quod maxime placeat facere possimus, omnis voluptas assumenda est, omnis dolor repellend mporibus autem quibusdam et aut officiis debitis aut rerum necessitatibus saepe eveniet ut et voluptates repudiandae sint et moles.</p>
  <span class="btn-ghost">Schedule an Appointment</span>
</section>

<section class="section blog">
  <h2 class="title">Recent Blog</h2>
  <article class="card" style="left:98px">
    <div class="ph" role="img" aria-label="Photo of a woman stretching her arms by the sea under a blue sky" style="background:linear-gradient(180deg,#9fcbe8,#d8ebf5 60%,#a89c88)"></div>
    <h3>Finibus Bonorumet Malorum</h3>
    <div class="meta"><span><svg><use href="#cal"/></svg>25/09/2017</span><span><svg><use href="#user"/></svg>John</span></div>
    <p>At vero eos et accusamus et iusto odio dignissimodu cimus qui blanditiis praesentium.</p>
    <span class="rm">READ MORE</span>
  </article>
  <article class="card" style="left:442px">
    <div class="ph" role="img" aria-label="Photo of a nurse checking an elderly woman's blood pressure" style="background:linear-gradient(120deg,#e9eef0,#cfd8dc 50%,#f1eeea)"></div>
    <h3>Finibus Bonorumet Malorum</h3>
    <div class="meta"><span><svg><use href="#cal"/></svg>25/09/2017</span><span><svg><use href="#user"/></svg>John</span></div>
    <p>At vero eos et accusamus et iusto odio dignissimodu cimus qui blanditiis praesentium.</p>
    <span class="rm">READ MORE</span>
  </article>
  <article class="card" style="left:787px">
    <div class="ph" role="img" aria-label="Photo of a senior couple walking hand in hand on a sandy beach" style="background:linear-gradient(180deg,#8fb9de,#c5dbe9 45%,#d9c7a3)"></div>
    <h3>Finibus Bonorumet Malorum</h3>
    <div class="meta"><span><svg><use href="#cal"/></svg>25/09/2017</span><span><svg><use href="#user"/></svg>John</span></div>
    <p>At vero eos et accusamus et iusto odio dignissimodu cimus qui blanditiis praesentium.</p>
    <span class="rm">READ MORE</span>
  </article>
</section>

<section class="section testi" role="img" aria-label="Testimonials over a blue-tinted photo of a woman jogging in a park">
  <h2 class="title">Testimonials</h2>
  <span class="arrow" style="left:30px"><svg viewBox="0 0 36 36"><path d="M20 11l-7 7 7 7" fill="none" stroke="#fff" stroke-width="2"/></svg></span>
  <span class="arrow" style="left:1132px"><svg viewBox="0 0 36 36"><path d="M15 11l7 7-7 7" fill="none" stroke="#fff" stroke-width="2"/></svg></span>
  <div class="quote" style="left:98px">
    <div class="avatar" role="img" aria-label="Portrait of the reviewer"></div>
    <p class="body">“ At vero eos et accusamus et iustodio dignissimos ducimus qui blanditiis praesent ium voluptatum deleniti atqu.</p>
    <div class="who">Marla Venditti</div>
    <div class="role">Financial Services Professional</div>
    <div class="stars"><svg><use href="#star"/></svg><svg><use href="#star"/></svg><svg><use href="#star"/></svg><svg><use href="#star"/></svg><svg><use href="#star-o"/></svg></div>
  </div>
  <div class="quote" style="left:445px">
    <div class="avatar" role="img" aria-label="Portrait of the reviewer" style="background:linear-gradient(160deg,#d8d8d8,#8d8d8d)"></div>
    <p class="body">“ At vero eos et accusamus et iustodio dignissimos ducimus qui blanditiis praesent ium voluptatum deleniti atqu.</p>
    <div class="who">Teodor R. Halvik</div>
    <div class="role">National Urban Fellow at the Harbor</div>
    <div class="stars"><svg><use href="#star"/></svg><svg><use href="#star"/></svg><svg><use href="#star"/></svg><svg><use href="#star"/></svg><svg><use href="#star-o"/></svg></div>
  </div>
  <div class="quote" style="left:792px">
    <div class="avatar" role="img" aria-label="Portrait of the reviewer"></div>
    <p class="body">“ At vero eos et accusamus et iustodio dignissimos ducimus qui blanditiis praesent ium voluptatum deleniti atqu.</p>
    <div class="who">Rosa Pellinger</div>
    <div class="role">Creative Strategist | Entrepreneur &amp; Speaker</div>
    <div class="stars"><svg><use href="#star"/></svg><svg><use href="#star"/></svg><svg><use href="#star"/></svg><svg><use href="#star"/></svg><svg><use href="#star-o"/></svg></div>
  </div>
</section>

<section class="section expect">
  <h2 class="title">What to Expect</h2>
  <div class="qa" style="left:98px"><div class="head">Finibus Bonorumet Malorum?</div><p>Nam libero tempore, cum soluta nobis essrt eligendi optio cumque nihil impedit quomin us id quod maxime placea.</p></div>
  <div class="qa hl" style="left:442px"><div class="head">Finibus Bonorumet Malorum?</div><p>Nam libero tempore, cum soluta nobis essrt eligendi optio cumque nihil impedit quomin us id quod maxime placea.</p></div>
  <div class="qa" style="left:787px"><div class="head">Finibus Bonorumet Malorum?</div><p>Nam libero tempore, cum soluta nobis essrt eligendi optio cumque nihil impedit quomin us id quod maxime placea.</p></div>
  <div class="dots"><i class="on"></i><i></i><i></i></div>
</section>

<footer class="section footer">
  <div class="totop"><svg viewBox="0 0 66 26"><path d="M0 26L33 4 66 26z" fill="#3a3a3a"/></svg>TO TOP</div>
  <h4 style="left:96px">Contact Form</h4>
  <div class="field" style="left:98px;top:202px;width:311px;height:32px">Name :</div>
  <div class="field" style="left:418px;top:202px;width:309px;height:32px">Phone no :</div>
  <div class="field" style="left:98px;top:247px;width:629px;height:32px">Email :</div>
  <div class="field" style="left:98px;top:291px;width:629px;height:81px">Message :</div>
  <span class="submit">SUBMIT</span>

  <h4 style="left:780px">Contact Information</h4>
  <div class="info" style="top:190px"><span class="ic"><svg viewBox="0 0 16 16"><path d="M8 1a5 5 0 0 0-5 5c0 4 5 9 5 9s5-5 5-9a5 5 0 0 0-5-5z" fill="#fff"/><circle cx="8" cy="6" r="1.8" fill="#2a2a2a"/></svg></span>412 Larchmont Way Brookfield MA 01506</div>
  <div class="info" style="top:248px"><span class="ic" style="color:#fff"><svg viewBox="0 0 16 16"><use href="#phone"/></svg></span>1 888 555 0142</div>
  <div class="info" style="top:301px"><span class="ic"><svg viewBox="0 0 16 16"><rect x="1.5" y="3.5" width="13" height="9" fill="#fff"/><path d="M1.5 3.5L8 9l6.5-5.5" fill="none" stroke="#2a2a2a" stroke-width="1.2"/></svg></span>hello@fernly.example</div>
  <div class="social" aria-label="Social media profiles">
    <span style="background:#3b5998"></span><span style="background:#1da1f2"></span><span style="background:#0e76a8"></span><span style="background:#cb2027"></span>
  </div>
  <div class="rule"></div>
  <p class="copy">Copyright © 2017, Fernly.&nbsp; All rights reserved.</p>
</footer>
</body>
</html>
```